Modern Lunetta Claims company

We need a new company presentation brochure, composed of about 20 pages in A4 format.
Cover, page 1 who we are, page 2 company profile, page 3 territorial operation, page from 4 to 10 services offered and description of services (The title of the page are: Perizie e Liquidazione danni, riparazioni e sostituzioni, teleclaimer, accertamento danni da fenomeno elettrico, TPA, Auditing, drone pilot, Valutazione rischi), from 11 to 17 specializations (Sinistri gravi, R.C., Tecnologici, Energie rinnovabili, strutture, ambiente) page 18 e 19 integrated services (perdite occulte, ricerca guasti, indagini termografiche, crisis management), page 20 clients ( list companies and logos) page 21 contact.
The company is made up of various companies, which belong to the principal, each of which deals with specific activities.
To date we already have various logos of the main company (Vardano and Pescetti) as well as the logos of the other companies. I load them on the portal.
Found then the graphic solution that we like we will have to proceed to make a presentation in similar powerpoint and the website.

Target Market(s)

Insurance Company, Insurance Broker

Font styles to use
Other font styles liked:
• ARIAL

Colors
333333
5c5c5c
959595
0392cd

Requirements
Must have
• It must be clear, professional and modern.
Nice to have
• I indicate some competitor sites, so that you can better understand what we are doing. www.torvellsgroup.example, www.harbridgeoakes.example, www.betadomaretti.example, www.gruppotavesi.example, www.vantuzzi.example.

```html
<!DOCTYPE html>
<html lang="en">
<head>
<meta charset="utf-8">
<title>Company Profile – Page 2</title>
<link href="https://fonts.googleapis.com/css2?family=Arimo:wght@400;700&display=swap" rel="stylesheet">
<style>
  :root {
    --frame: #333333;
    --frame-edge: #5c5c5c;
    --metal-light: #e6e7e9;
    --metal-mid: #c9cbce;
    --metal-dark: #a9abae;
    --brand-blue: #0a6fb7;
    --brand-blue-dark: #1f5e9c;
    --ink: #111111;
    --white: #ffffff;
  }
  * { box-sizing: border-box; margin: 0; padding: 0; }
  html, body { width: 847px; height: 1200px; overflow: hidden; }
  body {
    background: var(--frame);
    font-family: "Arimo", Arial, sans-serif;
    color: var(--ink);
  }
  .page {
    position: absolute;
    left: 18px; top: 20px;
    width: 811px; height: 1162px;
    border: 1px solid var(--frame-edge);
    background: linear-gradient(100deg, var(--metal-dark) 0%, var(--metal-mid) 22%, var(--metal-light) 48%, var(--metal-mid) 72%, var(--metal-dark) 100%);
  }
  .page-title {
    position: absolute;
    left: 2px; top: 20px;
    width: 400px; height: 33px;
    background: var(--brand-blue);
    border: 1px solid #4d94cf;
    color: var(--white);
    font-size: 23px;
    line-height: 31px;
    text-align: center;
  }
  .profile {
    position: absolute;
    left: 24px;
    width: 766px;
    font-size: 14.6px;
    line-height: 17.4px;
  }
  .profile--main { top: 143px; }
  .profile--partner { top: 372px; }
  .profile--claims { top: 598px; }
  .profile--assist { top: 824px; }
  .brand {
    float: left;
    display: flex;
    align-items: center;
    gap: 10px;
    color: var(--brand-blue-dark);
    font-weight: 700;
  }
  .brand--main { width: 420px; height: 68px; font-size: 31px; }
  .brand--partner { width: 323px; height: 78px; font-size: 25px; }
  .brand--claims { width: 173px; height: 90px; font-size: 20px; }
  .brand--assist { width: 123px; height: 70px; font-size: 18px; line-height: 20px; }
  .brand-mark-square { width: 44px; height: 44px; background: var(--brand-blue); flex: none; }
  .brand-mark-circle { width: 56px; height: 56px; border-radius: 50%; background: var(--brand-blue-dark); flex: none; }
  .folio {
    position: absolute;
    right: 22px; bottom: 26px;
    font-size: 16px;
  }
</style>
</head>
<body>
  <main class="page">
    <h1 class="page-title">Company Profile</h1>

    <section class="profile profile--main">
      <div class="brand brand--main">Vardano and Pescetti</div>
      <p>Sed ut perspiciatis unde omnis iste natus isisa error sit voluptatem accusantium doloremque laudantium, totam rem aperiam,eaque ipsa po quae ab illo inventore veritatis et quasi delmas architecto beatae vitae dicta sunt explicabo. Nemo enim ipsam voluptatem quia voluptas sit aspernatur aut odit aut fugit, sed quia consequuntur magni dolores eos qui ratione voluptatem sequi nesciunt. Mita Neque porro quisquam est, qui dolorem ipsum quia dolor sit amet, consectetur, adipisci velit, sed quia non numquam eius modi tempora incidunt ut labore et dolore magnam aliquam quaerat voluptatem. Re Ut enim ad minima veniam, quis nostrum exercitationem ullam corporis suscipit laboriosam, nisi ut eine aliquid ex ea commodi consequatur? Quis autem vel eum iure reprehenderit qui in ea voluptate velit for esse quam nihil molestiae consequatur, vel illum qui dolorem eum fugiat quo voluptas nulla pariatur?"</p>
    </section>

    <section class="profile profile--partner">
      <div class="brand brand--partner"><span class="brand-mark-circle"></span>Ostera Claims Partner</div>
      <p>Sed ut perspiciatis unde omnis iste natus error sit meine as voluptatem accusantium doloremque laudantium, totam pos rem aperiam,eaque ipsa quae ab illo inventore veritatis nei et quasi architecto beatae vitae dicta sunt explicabo. Nemo enim ipsam voluptatem quia voluptas sit aspernatur aut odit aut fugit, sed quia consequuntur magni opu dolores eos qui ratione voluptatem sequi nesciunt. Neque porro quisquam est, qui dolorem ipsum quia dolor sit amet, consectetur, adipisci velit, sed quia non numquam eius modi tempora incidunt ut labore et dolore magnam aliquam quaerat voluptatem. Ut enim ad minima veniam, quis nostrum magnum opu exercitationem ullam corporis suscipit laboriosam, nisi ut aliquid ex ea commodi consequatur? Quis iso autem vel eum iure reprehenderit qui in ea voluptate velit esse quam nihil molestiae consequatur, veller illum qui dolorem eum fugiat quo voluptas nulla pariatur?"</p>
    </section>

    <section class="profile profile--claims">
      <div class="brand brand--claims">Lunetta Claims</div>
      <p>Sed ut perspiciatis unde omnis iste natus error sit meine as consequuntur miene voluptatem accusantium doloremque laudantium, totam pos consequuntur opus rem aperiam,eaque ipsa quae ab illo inventore veritatis nei consequuntur magni et quasi architecto beatae vitae dicta sunt explicabo. Nemo consequuntur magni enim ipsam voluptatem quia voluptas sit aspernatur aut odit aut fugit, sed quia consequuntur magni opu dolores eos qui ratione voluptatem sequi nesciunt. Neque porro quisquam est, qui dolorem ipsum quia dolor sit amet, consectetur, adipisci velit, sed quia non numquam eius modi tempora incidunt ut labore a et dolore magnam aliquam quaerat voluptatem. Ut enim ad minima veniam, quis nostrum magnum opu exercitationem ullam corporis suscipit laboriosam, nisi ut aliquid ex ea commodi consequatur? Quis iso autem vel eum iure reprehenderit qui in ea voluptate velit esse quam nihil molestiae consequatur, veller illum qui dolorem eum fugiat quo voluptas nulla pariatur?"</p>
    </section>

    <section class="profile profile--assist">
      <div class="brand brand--assist">Corvina Assist</div>
      <p>Sed ut perspiciatis unde omnis iste natus error sit meine as consequuntur magni opu o voluptatem accusantium doloremque laudantium, totam pos consequuntur magni opu i rem aperiam,eaque ipsa quae ab illo inventore veritatis nei consequuntur magni opu s et quasi architecto beatae vitae dicta sunt explicabo. Nemo consequuntur magni opu if enim ipsam voluptatem quia voluptas sit aspernatur aut odit aut fugit, sed quia consequuntur magni opu dolores eos qui ratione voluptatem sequi nesciunt. Neque porro quisquam est, qui dolorem ipsum quia dolor sit amet, consectetur, adipisci velit, sed quia non numquam eius modi tempora incidunt ut labore a et dolore magnam aliquam quaerat voluptatem. Ut enim ad minima veniam, quis nostrum magnum opu exercitationem ullam corporis suscipit laboriosam, nisi ut aliquid ex ea commodi consequatur? Quis iso autem vel eum iure reprehenderit qui in ea voluptate velit esse quam nihil molestiae consequatur, veller illum qui dolorem eum fugiat quo voluptas nulla pariatur?"</p>
    </section>

    <footer class="folio">Page 2</footer>
  </main>
</body>
</html>
```